Die Morgenfalter - ein Wissenschaftsthriller sucht ein tolles Buchcover
Die Zusammenarbeit war einfach und das Ergebnis war verblüffend genial. Gute Ideen, schnelle Umsetzung und sie versteht es Vorschläge in das Design einfliessen zu lassen! Jederzeit wieder. Sorry für die späte Bewertung.
Zielgruppe
Das Buch (Print und E-Book+Vorschaugrafik) 'Die Morgenfalter' sucht dringend ein neues Cover. Zielgruppe sind sowohl Leser/innen die nach einem spannenden 'High Tech' Thriller in den Buchhandlungen suchen, als auch Leser die einen E-Book Reader benutzen und für relativ wenig Geld auch mal ein Experiment einkaufen (Debütthriller)- Hier muß das Cover sehr schnell 'Aufmerksamkeit' erregen beim blättern im Web und in den Katalogen!
Wichtig ist, es handelt sich nicht um einen reinen Science Fiction Thriller, es ist ein realitätsnahes Buch und soll eine breite Leserschaft ansprechen.
Die Handlung könnte im hier und jetzt spielen, es geht um Quantencomputer, Hacker, Industriespionage, Computerchips und Wirtschaftskriminalität.
Das Buch hat 560 Seiten!
Mehr über das Buch unter www.morgenfalter-roman.com
Hier der Klappentext auf die schnelle:
Das Buch
Fesselnd, abwechslungsreich und informativ. Das Buch skizziert eine beängstigende Verschwörung im Rahmen des weltweiten Cyber- War. Ein Szenario das morgen durchaus Realität werden könnte. Detailliert und brutal beschreibt der Autor wie die Supermächte versuchen die Welt 2.0 zu kontrollieren und zu beherrschen.
+++++++ Die Story +++++++++++++++++++++ Die Story +++++++++++
Felix Obermann arbeitet als Spezialist für Halbleitertechnologie für das Unternehmen Polaris Markt Analytik. Während er für die auf internationales Patentrecht spezialisierte Kanzlei von Ewald Halberg eine Marktanalyse für Netzwerkchips erstellt, erfährt er von einem Informanten, dass der berühmte Wissenschaftler Benedikt Sauer tot in einem Kanal in Bangkok gefunden wurde. Angeblich hat er eine wissenschaftliche Entdeckung mit in sein nasses Grab genommen.
Als Felix Obermann ein Angebot von der Kanzlei Halberg für eine Zusammenarbeit bekommt, ändert sich sein bis dahin eher langweiliges Leben schlagartig. Als Partnerin bekommt er die geheimnisvolle Ilka ter Huis an seine Seite. Der erste ..
Aufgabenstellung
Anbei ein paar alte Cover, Bilder die Sie benutzen können, ein Mastercover wegen Größe von Folio Dock und Texte. Als Ergebnis möchte ich folgendes bekommen:
- Ein Buchcover komplett- fertig und geeignet für den Druck über den Folio Dock Service. Als Art ist matt-glossy meine bevorzugte Einstellung. Die Datei muß .pdf (Druckformat – bitte Farbeinstellung beachten!) sein
- Meine gewählte Buchgröße ist (5,0x8,0 d.h.12,7x20,32), anbei eine Datei die die gesamte Größe darstellt. Es sind insgesamt 280 einzelne Seiten- bei der Berechnung vom Spin beachten! (560 Seiten zum lesen)
- Ein E-Book Cover (.jpg) optimiert für E-Reader (d.h. es sollte nicht so eine riesige Datei sein und insgesamt ein wenig skalierbar hinsichtlich Größe)
- eine Vorschaugrafik von dem Cover (vielleicht 300*500 Pixel o.ä.)
Das Cover sollte sowohl „ Leben“ zeigen (vielleicht ein paar schattierte Menschen i m Hintergrund?), als auch den wissenschaftlichen Hintergrund ( Computerchips etc.)
Aus meiner kleinen Umfrage habe ich folgendes mitgenommen:
Das alte Cover ( nur schwarz mit einer symbolhaften Leiterplatte in rot) erzeugt zu wenig Aufmerksamkeit, zu Langweilig, keine Aussagekraft, zu technisch!
Das zweite Cover mit dem blauen Würfel vorne und der Buchrückseite mit dem Chip ist viel besser, aber immer noch zu „tot“, es fehlt Leben?
Das Pop Art Cover in knallbunt ist wohl der totale Missgriff….;(
Man kann es nicht jedem recht machen, aber Aufmerksamkeit, Technologiebezug und ein wenig Leben auf dem Bild, eine als Druckvorlage geeignete Datei, ein handwerklich gekonntes E-Book Cover Design und eine Vorschaugrafik die auch als solche zu erkennen ist, sollte möglich sein.
Ein wichtiger Hinweis noch: Das Projekt ist dann beendet, wenn die Cover Datei funktioniert bei Folio Dock und das gedruckte Buchcoverokay ist, d.h. wenn es soweit ist, ordere ich ein Buch und die Qualität muss stimmen (Auflösung ..

```html
<!DOCTYPE html>
<html lang="de">
<head>
<meta charset="utf-8">
<title>Die Morgenfalter – Buchumschlag</title>
<link rel="stylesheet" href="https://fonts.googleapis.com/css2?family=Anton&family=Passion+One:wght@700&family=Alfa+Slab+One&family=PT+Sans+Narrow:wght@400;700&display=swap">
<style>
  :root {
    --night: #020204;
    --deep-blue: #1a1a6e;
    --violet: #4a2bb0;
    --glow-cyan: #3fd6e8;
    --title-yellow: #f2e61c;
    --author-cyan: #7fd3da;
    --thriller-red: #c0302a;
    --body-white: #f1f1f1;
    --cube-blue: #2a5fd0;
  }
  * { margin: 0; padding: 0; box-sizing: border-box; }
  html, body { width: 1200px; height: 867px; overflow: hidden; background: var(--night); }
  .cover-wrap {
    position: relative;
    width: 1200px; height: 867px;
    overflow: hidden;
    background:
      radial-gradient(ellipse 420px 300px at 1150px 40px, rgba(63,214,232,0.45), transparent 70%),
      linear-gradient(180deg, var(--night) 0%, #05051a 35%, var(--deep-blue) 72%, var(--violet) 100%);
  }
  /* back cover */
  .back-block { position: absolute; left: 66px; width: 440px; color: var(--body-white); font-family: "PT Sans Narrow", sans-serif; }
  .block-story { top: 110px; }
  .block-reality { top: 345px; }
  .block-opinions { top: 480px; }
  .back-heading { font-weight: 700; color: var(--title-yellow); font-size: 18px; line-height: 22px; margin-bottom: 4px; }
  .back-text { font-size: 13px; line-height: 21px; text-align: justify; }
  .quote { margin-bottom: 21px; }
  /* spine */
  .spine { position: absolute; left: 542px; top: 0; width: 84px; height: 867px; }
  .spine-title {
    position: absolute; left: 16px; top: 116px;
    writing-mode: vertical-rl;
    font-family: "Anton", sans-serif; font-size: 38px; line-height: 1;
    color: var(--title-yellow); letter-spacing: 1px;
  }
  .spine-author {
    position: absolute; left: 32px; top: 520px;
    writing-mode: vertical-rl;
    font-family: "Passion One", sans-serif; font-weight: 700; font-size: 25px; line-height: 1;
    color: var(--author-cyan); letter-spacing: 1.5px;
  }
  /* front cover */
  .front-art { position: absolute; left: 700px; top: 70px; width: 420px; height: 470px; }
  .front-title {
    position: absolute; left: 690px; top: 588px;
    font-family: "Anton", sans-serif; font-size: 86px; line-height: 84px;
    color: var(--title-yellow); text-transform: uppercase; white-space: nowrap;
  }
  .front-author {
    position: absolute; left: 824px; top: 606px;
    font-family: "Passion One", sans-serif; font-weight: 700; font-size: 43px; line-height: 1;
    color: var(--author-cyan); letter-spacing: 1px; white-space: nowrap;
  }
  .front-genre {
    position: absolute; left: 692px; top: 772px;
    font-family: "Alfa Slab One", serif; font-size: 39px; line-height: 1;
    color: var(--thriller-red); white-space: nowrap;
  }
</style>
</head>
<body>
<main class="cover-wrap">

  <section class="back-block block-story">
    <h2 class="back-heading">Mord und Intrigen in der Welt der Chip-Technologien</h2>
    <p class="back-text">Eben noch hat Felix Obermann an seinem Schreibtisch in Hamburg eine Marktanalyse für Netzwerkchips erstellt, jetzt findet sich der Spezialist für Halbleitertechnologie plötzlich in einem undurchsichtigen Strudel aus Mord, Korruption und Intrigen wieder. Nach dem mysteriösen Tod eines renommierten amerikanischen Quanteninformatikers in Thailand sollen er und seine Partnerin Ilka ter Huis im Auftrag eines internationalen Konsortiums herausfinden, was es mit einer neuen Generation von Chips auf sich hat – der ermordete Wissenschaftler arbeitete angeblich an deren Herstellung. Noch ahnt Obermann nicht, auf was er sich da eingelassen hat.</p>
  </section>

  <section class="back-block block-reality">
    <h2 class="back-heading">Die Realität!</h2>
    <p class="back-text">Das Buch skizziert eine beängstigende Verschwörung im Rahmen des weltweiten Cyber- War. Ein Szenario das Realität werden könnte. Detailliert und brutal beschreibt der Autor wie die Supermächte versuchen die Welt 2.0 zu kontrollieren und zu beherrschen.</p>
  </section>

  <section class="back-block block-opinions">
    <h2 class="back-heading">Meinungen</h2>
    <p class="back-text quote">Spannender, zeitgemäßer Wissenschafts-Thriller<br>Jonas Wehrmann hat mit „Die Morgenfalter“ einen realitätsnahen- und spannenden Wissenschaftsthriller geschrieben, der im Genre „Thriller“ einen sicheren Platz einnehmen darf. Er setzt mit seinem Buch eine erschreckende Szenerie der Wissenschaftsspionage ins Bild. (Buchpalast)</p>
    <p class="back-text quote">Im Kampf um die Macht zählt ein Menschenleben nichts- brisantes Thema gut aufgearbeitet (Leseinsel)</p>
    <p class="back-text quote">Der Debütroman enthält alle klassischen Elemente eines Thrillers. Es dreht sich gleichermaßen um Forschung, Quanteninformatik und Halbleitertechnik wie um Verschwörung, Korruption und Mord ! Chipfokus 1/15</p>
  </section>

  <section class="spine">
    <span class="spine-title">DIE MORGENFALTER</span>
    <span class="spine-author">JONAS WEHRMANN</span>
  </section>

  <section class="front-cover">
    <svg class="front-art" viewBox="0 0 420 470" role="img" aria-label="Illustration: leuchtend blauer Glaswürfel mit Leiterbahnen, darüber ein roter Handabdruck">
      <defs>
        <linearGradient id="cubeTone" x1="0" y1="0" x2="1" y2="1">
          <stop offset="0" stop-color="#4f8fe8"/>
          <stop offset="0.6" stop-color="var(--cube-blue)"/>
          <stop offset="1" stop-color="#15307a"/>
        </linearGradient>
      </defs>
      <rect x="10" y="30" width="400" height="436" rx="14" fill="url(#cubeTone)" opacity="0.85"/>
    </svg>
    <h1 class="front-title">Die<br>Morgenfalter</h1>
    <p class="front-author">JONAS WEHRMANN</p>
    <p class="front-genre">Wissenschaftsthriller</p>
  </section>

</main>
</body>
</html>
```